Pelton Mortgage Capital Business Card

We need a business card design for our mortgage servicing company. In addition to servicing the loans of homeowners, we help homeowners with purchasing their homes and any mortgage refinancing. We would like to see designs that use the colors in the logo attached below (gold-ish yellow and navy blue), and any other design you deem fit! The design should communicate a simpler life with smart mortgages provided by Pelton.

```html
<!DOCTYPE html>
<html lang="en">
<head>
<meta charset="utf-8">
<title>Pelton Mortgage Capital Business Card</title>
<link href="https://fonts.googleapis.com/css2?family=Open+Sans:wght@400;600;700&display=swap" rel="stylesheet">
<style>
  :root {
    --navy: #262057;
    --navy-light: #3a3378;
    --gold: #d9a82b;
    --ink: #4a4a4a;
    --paper: #fbfbfb;
    --backdrop: #e6e6e6;
  }
  * { margin: 0; padding: 0; box-sizing: border-box; }
  html, body { width: 1200px; height: 801px; overflow: hidden; }
  body {
    background: var(--backdrop);
    font-family: "Open Sans", Arial, sans-serif;
    position: relative;
  }
  .card {
    position: absolute;
    top: 250px;
    width: 520px;
    height: 300px;
    box-shadow: 0 6px 18px rgba(0,0,0,0.18);
  }
  .card--front { left: 50px; background: var(--paper); }
  .card--back { left: 630px; background: var(--navy); display: flex; align-items: center; justify-content: center; }

  .brand {
    position: absolute;
    left: 0; top: 0;
    width: 260px; height: 300px;
    display: flex; align-items: center; justify-content: center;
    gap: 10px;
  }
  .brand__dot { width: 14px; height: 14px; border-radius: 50%; background: var(--gold); }
  .brand__name {
    font-weight: 700;
    font-size: 34px;
    color: var(--gold);
    letter-spacing: 0.5px;
  }
  .divider {
    position: absolute;
    left: 268px; top: 42px;
    width: 1px; height: 216px;
    background: var(--navy);
  }
  .details {
    position: absolute;
    left: 290px; top: 46px;
    width: 220px;
    color: var(--ink);
  }
  .details__name { font-weight: 700; font-size: 17px; color: var(--navy); letter-spacing: 0.3px; }
  .details__role { font-size: 13px; color: var(--gold); margin-top: 2px; }
  .details__address { font-size: 13px; line-height: 1.45; margin-top: 18px; }
  .contact { list-style: none; margin-top: 18px; font-size: 13px; line-height: 1.6; }
  .contact li { display: flex; align-items: center; gap: 8px; }
  .contact svg { width: 10px; height: 10px; fill: var(--gold); flex: none; }

  .back-brand {
    font-weight: 700;
    font-size: 60px;
    color: var(--navy-light);
    letter-spacing: 1px;
  }
</style>
</head>
<body>
  <section class="card card--front" aria-label="Card front">
    <div class="brand">
      <span class="brand__dot"></span>
      <span class="brand__name">Pelton Mortgage</span>
    </div>
    <div class="divider"></div>
    <div class="details">
      <p class="details__name">DORIAN WEXLEY</p>
      <p class="details__role">President</p>
      <p class="details__address">18320 Harbor View Dr<br>Bayside CA 92071</p>
      <ul class="contact">
        <li><svg viewBox="0 0 10 10"><path d="M2 0.5 L4 2.8 L3 4 Q4 6 6 7 L7.2 6 L9.5 8 L8 9.6 Q3 9 0.4 2 Z"/></svg>555-318-4720</li>
        <li><svg viewBox="0 0 10 10"><path d="M0 2 H10 V8 H0 Z M0 2 L5 5.5 L10 2" stroke="#fbfbfb" stroke-width="0.8"/></svg>info@PeltonMortgage.com</li>
        <li><svg viewBox="0 0 10 10"><circle cx="5" cy="5" r="4.5"/></svg>www.PeltonMortgage.com</li>
      </ul>
    </div>
  </section>

  <section class="card card--back" aria-label="Card back">
    <span class="back-brand">Pelton Mortgage</span>
  </section>
</body>
</html>
```